buisnes card for Tranquil Footpath

I need a new business card with my information
Brunhilde Ostrova
BKTPA,LMVD,RN(Grermany)
Cranio-Sacral Reflexology
Facial Reflexology, Halvorkmethode TM
Nerve point Reflexology
41672 Meadowcroft Lane
Abbotsford,BC
Tranquilfootpath.ca
I would like the design to show that I work mostly with clients that have health problems.(80% are back/spine related problems).
I would like the card to be professional as well as inviting. I like nature aspects as well.
I have two websites that I like so you have an Idea what kind of design speaks to me.
1. www.harmonelle.ca the craft of mending (Chilliwack)
2.www.gentlearrivalcare.ca (Abbotsford)

My treatment room is blue and the outside of our house is dark blue and grey. That are colors that could be incorporated

Target Market(s)

clients that are looking for a more natural approach to their health issues

Industry/Entity Type

Health And Wellness

Contact Information for Business Card

Brunhilde Ostrova
BKTPA,LMVD,RN(Grermany)
Cranio-Sacral Reflexology
Nerve point Reflexology
41672 Meadowcroft Lane
Abbotsford,BC
Tranquilfootpath.ca

Colors
0355a3
0492cd

Requirements
Must have
• name, address, phonenumber
Nice to have
• 1. www.harmonelle.ca the craft of mending (Chilliwack)
• 2.www.gentlearrivalcare.ca (Abbotsford)
• This are designs that I like.

```html
<!DOCTYPE html>
<html lang="en">
<head>
<meta charset="utf-8">
<title>Tranquil Footpath – Business Card</title>
<link rel="stylesheet" href="https://fonts.googleapis.com/css2?family=Arimo:wght@400;700&display=swap">
<style>
  :root {
    --page-bg: #1b1b1b;
    --sky-blue: #0492cd;
    --mid-blue: #0a72bb;
    --deep-blue: #0355a3;
    --band-white: #ffffff;
    --text-light: #ffffff;
    --text-blue: #0355a3;
  }
  * { margin: 0; padding: 0; box-sizing: border-box; }
  html, body {
    width: 1200px;
    height: 902px;
    overflow: hidden;
    background: var(--page-bg);
    font-family: "Arimo", Arial, Helvetica, sans-serif;
  }
  .business-card {
    position: absolute;
    left: 40px;
    top: 132px;
    width: 1120px;
    height: 637px;
    overflow: hidden;
    background: linear-gradient(180deg, var(--mid-blue) 0%, var(--deep-blue) 100%);
  }
  .card-top {
    position: absolute;
    left: 0; top: 0;
    width: 100%;
    height: 188px;
    background: linear-gradient(180deg, var(--sky-blue) 0%, var(--mid-blue) 100%);
  }
  .wave-texture {
    position: absolute;
    right: 0; top: 0;
    width: 560px;
    height: 637px;
    background: radial-gradient(ellipse at 85% 40%, rgba(255,255,255,0.14) 0%, rgba(255,255,255,0) 70%);
  }
  .rule {
    position: absolute;
    left: 0;
    width: 100%;
    height: 5px;
    background: var(--band-white);
  }
  .rule--upper { top: 188px; }
  .rule--lower { top: 402px; }
  .name-band {
    position: absolute;
    left: 0;
    top: 199px;
    width: 100%;
    height: 196px;
    background: var(--band-white);
  }
  .body-figure {
    position: absolute;
    left: 20px;
    top: 58px;
    width: 482px;
    height: 579px;
    border-radius: 200px 200px 0 0;
    background: radial-gradient(ellipse at 50% 40%, #6fb4f0 0%, #2f7fd0 45%, rgba(3,85,163,0) 75%);
  }
  .line {
    position: absolute;
    right: 63px;
    line-height: 1;
    white-space: nowrap;
    text-align: right;
  }
  .services { font-size: 26px; color: var(--text-light); }
  .services--one { top: 74px; }
  .services--two { top: 112px; }
  .practitioner-name {
    top: 250px;
    font-size: 45px;
    font-weight: 700;
    color: var(--text-blue);
  }
  .credentials {
    top: 310px;
    font-size: 25px;
    color: var(--text-blue);
  }
  .address { font-size: 30px; color: var(--text-light); }
  .address--street { top: 453px; }
  .address--city { top: 495px; }
  .website {
    top: 565px;
    font-size: 30px;
    font-weight: 700;
    color: var(--text-light);
  }
</style>
</head>
<body>
  <main class="business-card">
    <div class="card-top"></div>
    <div class="wave-texture" role="img" aria-label="Fine curved wireframe lines sweeping across the right side"></div>
    <div class="rule rule--upper"></div>
    <div class="name-band"></div>
    <div class="rule rule--lower"></div>
    <div class="body-figure" role="img" aria-label="Blue x-ray style human figure showing the skeleton and spine, with joints highlighted in red"></div>

    <p class="line services services--one">Cranio-Sacral Reflexology-Facial Reflexology</p>
    <p class="line services services--two">Halvorkmethode TM-Nerve point Reflexology</p>

    <h1 class="line practitioner-name">BRUNHILDE OSTROVA</h1>
    <p class="line credentials">BKTPA,LMVD,RN(Grermany)</p>

    <p class="line address address--street">41672 Meadowcroft Lane</p>
    <p class="line address address--city">Abbotsford,BC</p>
    <p class="line website">Tranquilfootpath.ca</p>
  </main>
</body>
</html>
```